Brackenfield Partners Exit Plan business consultant web site

This website is for a consulting business that helps other businesses with exit plans. Essentially, assists them with the sale of their business. This website should be very professional, almost with a wall street look. I would like a very attractive image on the homepage. Perhaps something that denotes success. Perhaps a picture of palm trees and a beach? I will leave it to you for interpretation.

Across the screen I would like the words "Does your business have an exit plan?"

Below that it should read the following:
Let us help you with a completely impartial, no obligation assessment (button with link to the contact page)

Also, please use logo in a prominent place on the website so it's easily seen.

Target Market(s)

Males 40+

Coding

Coded - Design and coding required

Number of Pages Required

5+ page

Colors

Designer to choose colors to be used in the design.

Requirements
Must have
• The tabs for the homepage on the top should be:
• 1. About us
• 2. Services
• 3. Industries
• 4. Our success
• 5. Contact
Nice to have
• Clean, professional image.
• Please put FB, Chirpline, Linked In - logos at bottom.
• Here are two examples of a website to give you an idea:
• https://journal.corvanteriq.com/library/why-every-business-owner-should-have-an-exit-plan
Should not have
• nothing whimsical or cartoon like

```html
<!DOCTYPE html>
<html lang="en">
<head>
<meta charset="utf-8">
<title>Brackenfield Partners</title>
<link href="https://fonts.googleapis.com/css2?family=IBM+Plex+Sans:wght@400;500;600;700&display=swap" rel="stylesheet">
<style>
:root{
  --ink:#111111;
  --paper:#ffffff;
  --mist:#f3f0f0;
  --charcoal:#1f1f1f;
  --stone:#dedede;
  --rule:#a8a8a8;
  --muted:#444444;
  --sand:#e9e0cf;
}
*{margin:0;padding:0;box-sizing:border-box}
html,body{width:1200px;height:3405px;overflow:hidden}
body{position:relative;font-family:"IBM Plex Sans",Arial,sans-serif;color:var(--ink);background:var(--paper)}
.abs{position:absolute}

/* hero */
.hero{position:absolute;left:0;top:0;width:1200px;height:649px;overflow:hidden}
.hero-photo{position:absolute;inset:0;background:linear-gradient(180deg,#7fb0dc 0%,#c9def0 30%,#e8eef3 44%,#52c0c8 50%,#2f9fb0 62%,#8fd0cc 70%,#e7dfcf 80%,var(--sand) 100%)}
.nav-rule{position:absolute;top:47px;height:1px;background:var(--ink)}
.nav a{position:absolute;top:62px;font-weight:600;font-size:16px;color:var(--ink);text-decoration:none;letter-spacing:.2px}
.nav a.active{text-decoration:underline;text-underline-offset:4px}
.brand-mark{position:absolute;left:568px;top:30px;width:64px;height:64px;background:var(--ink)}
.brand-name{position:absolute;left:400px;width:400px;top:114px;text-align:center;font-size:24px;font-weight:500;letter-spacing:.5px;color:var(--ink)}
.hero h1{position:absolute;left:222px;top:232px;font-size:43px;line-height:45px;font-weight:700;text-transform:uppercase}
.hero .lead{position:absolute;left:222px;top:386px;font-size:18px;line-height:25.5px;font-weight:700;text-transform:uppercase;color:#1a1a1a}
.btn-solid{position:absolute;left:223px;top:488px;width:155px;height:50px;background:var(--ink);color:var(--paper);font-weight:700;font-size:18px;display:flex;align-items:center;justify-content:center}

/* section titles */
.section-title{position:absolute;left:0;width:1200px;text-align:center;font-size:30px;font-weight:700;letter-spacing:.3px}
.section-bar{position:absolute;left:580px;width:40px;height:4px;background:var(--rule)}

/* services */
.services{position:absolute;left:0;top:649px;width:1200px;height:646px;background:var(--mist)}
.service-card{position:absolute;width:458px;height:216px;background:var(--paper);box-shadow:0 0 6px rgba(0,0,0,.12)}
.service-card::after{content:"";position:absolute;inset:7px;border:1px solid #d8d8d8}
.service-icon{position:absolute;left:40px;top:36px;width:80px;height:80px;border-radius:50%;background:#ececec;display:flex;align-items:center;justify-content:center}
.service-card h3{position:absolute;left:158px;top:36px;font-size:16.5px;font-weight:600}
.service-card p{position:absolute;left:158px;top:64px;width:250px;font-size:13px;line-height:17.6px;color:#333}
.btn-outline{position:absolute;left:159px;top:155px;width:95px;height:26px;border:1.5px solid var(--ink);font-size:12.5px;font-weight:500;display:flex;align-items:center;justify-content:center;z-index:1}

/* welcome */
.welcome-mark{position:absolute;left:190px;top:1366px;width:302px;height:363px;background:var(--ink);display:flex;align-items:center;justify-content:center}
.welcome-mark::after{content:"";position:absolute;inset:9px;border:3px solid var(--paper)}
.welcome-mark span{color:var(--paper);font-size:30px;font-weight:600;text-align:center;line-height:40px}
.welcome-kicker{position:absolute;left:575px;top:1360px;font-size:21px;font-weight:500}
.welcome-title{position:absolute;left:575px;top:1392px;font-size:35px;font-weight:700;letter-spacing:.3px;white-space:nowrap}
.welcome-copy{position:absolute;left:576px;top:1496px;width:460px;font-size:14.5px;line-height:22.4px;color:#333}
.btn-double{position:absolute;left:577px;top:1686px;width:110px;height:47px;border:1.5px solid var(--ink);padding:3px}
.btn-double span{display:flex;width:100%;height:100%;background:var(--ink);color:var(--paper);font-size:13px;font-weight:600;align-items:center;justify-content:center}

/* industries */
.industries{position:absolute;left:0;top:1805px;width:1200px;height:602px;background:var(--charcoal)}
.industry-card{position:absolute;top:147px;width:219px;height:326px;background:var(--paper)}
.industry-photo{height:205px}
.industry-card h4{position:absolute;top:230px;width:100%;text-align:center;font-size:14px;font-weight:600}
.industry-card p{position:absolute;top:256px;left:20px;right:20px;text-align:center;font-size:12px;line-height:14.5px;color:#333}
.btn-light{position:absolute;left:511px;top:513px;width:178px;height:44px;border:1.5px solid var(--paper);padding:3px}
.btn-light span{display:flex;height:100%;background:var(--paper);font-size:12.5px;font-weight:600;align-items:center;justify-content:center}

/* success */
.success{position:absolute;left:0;top:2407px;width:1200px;height:600px;background:var(--stone)}
.quote-shadow{position:absolute;left:145px;top:2549px;width:915px;height:325px;background:#c4c4c4}
.quote-card{position:absolute;left:132px;top:2557px;width:936px;height:308px;background:var(--paper)}
.quote-glyph{position:absolute;font-size:110px;font-weight:700;color:#b8b8b8;line-height:1}
.quote-text{position:absolute;top:58px;width:325px;font-size:14.5px;line-height:20.8px;color:#333}
.quote-divider{position:absolute;left:468px;top:40px;width:1px;height:228px;background:#cfcfcf}
.quote-author{position:absolute;top:236px;font-size:14px}
.quote-author::before{content:"";position:absolute;left:-58px;top:10px;width:39px;height:2px;background:var(--ink)}
.quote-author small{display:block;font-size:12px;color:#555;margin-left:3px}
.dot{position:absolute;top:2919px;width:8px;height:8px;border-radius:50%;background:#b4b4b4}
.dot.on{background:var(--ink)}

/* footer */
.footer{position:absolute;left:0;top:2980px;width:1200px;height:425px;background:#000;color:var(--paper)}
.footer-mark{position:absolute;left:132px;top:90px;width:169px;height:204px;border:3px solid var(--paper);display:flex;align-items:center;justify-content:center}
.footer-mark::after{content:"";position:absolute;inset:6px;border:2px solid var(--paper)}
.footer-mark span{font-size:19px;font-weight:600;text-align:center;line-height:26px}
.footer h5{position:absolute;top:92px;font-size:16.5px;font-weight:700;letter-spacing:.3px}
.social{position:absolute;left:410px;display:flex;align-items:center;gap:15px;font-size:14px;line-height:18px}
.social i,.contact-item i{display:block;width:28px;height:28px;border-radius:50%;background:var(--paper);flex:none}
.footer-menu{position:absolute;left:654px;top:135px;list-style:none;font-size:14.5px;line-height:20.8px;color:#ddd}
.contact-item{position:absolute;left:858px;display:flex;align-items:center;gap:16px;font-size:12.5px;line-height:16px}
.contact-item i{width:34px;height:34px;display:flex;align-items:center;justify-content:center}
.contact-item b{font-size:14px;font-weight:600}
.footer-rule{position:absolute;left:132px;top:349px;width:936px;height:1px;background:#555}
.copyright{position:absolute;left:0;top:387px;width:1200px;text-align:center;font-size:11.5px;color:#ccc}
</style>
</head>
<body>

<header class="hero">
  <div class="hero-photo" role="img" aria-label="Tropical beach with turquoise sea and white sand under a bright cloudy sky, a businessman in a suit walking away along the shore"></div>
  <div class="nav-rule" style="left:225px;width:275px"></div>
  <div class="nav-rule" style="left:685px;width:333px"></div>
  <nav class="nav">
    <a class="active" style="left:227px">HOME</a>
    <a style="left:308px">ABOUT US</a>
    <a style="left:427px">SERVICES</a>
    <a style="left:685px">INDUSTRIES</a>
    <a style="left:810px">OUR SUCCESS</a>
    <a style="left:946px">CONTACT</a>
  </nav>
  <div class="brand-mark"></div>
  <div class="brand-name">Brackenfield Partners</div>
  <h1>Does your<br>business have<br>an exit plan?</h1>
  <p class="lead">Let us help you with a<br>completely impartial, no<br>obligation assessment</p>
  <a class="btn-solid">CONTACT US</a>
</header>

<section class="services">
  <h2 class="section-title" style="top:42px">OUR SERVICES</h2>
  <div class="section-bar" style="top:93px"></div>

  <article class="service-card" style="left:131px;top:143px">
    <div class="service-icon"><svg width="50" height="50" viewBox="0 0 50 50" fill="none" stroke="#111" stroke-width="3"><circle cx="21" cy="21" r="14"/><circle cx="21" cy="21" r="9"/><path d="M31 31l12 12" stroke-width="5"/><path d="M16 25v-3M20 25v-6M24 25v-8" stroke-width="2.5"/></svg></div>
    <h3>BUSINESS ANALYSIS</h3>
    <p>Lorem ipsum dolor sit amet, conse ctetur adipiscing elit, sed do eiusmod tempor incididunt ut labore et dolore magna aliqua.</p>
    <a class="btn-outline">READ MORE</a>
  </article>
  <article class="service-card" style="left:611px;top:143px">
    <div class="service-icon"><svg width="50" height="50" viewBox="0 0 50 50" fill="none" stroke="#111" stroke-width="3"><path d="M10 26a15 15 0 0 1 30 0"/><rect x="6" y="24" width="8" height="12" rx="2" fill="#111"/><rect x="36" y="24" width="8" height="12" rx="2" fill="#111"/><path d="M40 36c0 6-6 8-12 8"/></svg></div>
    <h3>CUSTOMER SERVICE</h3>
    <p>Lorem ipsum dolor sit amet, conse ctetur adipiscing elit, sed do eiusmod tempor incididunt ut labore et dolore magna aliqua.</p>
    <a class="btn-outline">READ MORE</a>
  </article>
  <article class="service-card" style="left:131px;top:381px">
    <div class="service-icon"><svg width="50" height="50" viewBox="0 0 50 50" fill="#111"><path d="M4 10h26v17H15l-7 7v-7H4z"/><path d="M34 16h12v17h-4v7l-7-7H20v-3h14z"/></svg></div>
    <h3>CONSULTANCY SERVICES</h3>
    <p>Lorem ipsum dolor sit amet, conse ctetur adipiscing elit, sed do eiusmod tempor incididunt ut labore et dolore magna aliqua.</p>
    <a class="btn-outline">READ MORE</a>
  </article>
  <article class="service-card" style="left:611px;top:381px">
    <div class="service-icon"><svg width="50" height="50" viewBox="0 0 50 50" fill="none" stroke="#111" stroke-width="3"><rect x="14" y="8" width="30" height="22"/><path d="M29 30v6M22 44l7-8 7 8M19 20l7-5 5 4 8-6"/></svg></div>
    <h3>EXECUTIVE COACHING</h3>
    <p>Lorem ipsum dolor sit amet, conse ctetur adipiscing elit, sed do eiusmod tempor incididunt ut labore et dolore magna aliqua.</p>
    <a class="btn-outline">READ MORE</a>
  </article>
</section>

<section class="welcome">
  <div class="welcome-mark"><span>Brackenfield<br>Partners</span></div>
  <p class="welcome-kicker">WELCOME TO</p>
  <h2 class="welcome-title">BRACKENFIELD PARTNERS</h2>
  <div class="section-bar" style="left:577px;top:1456px"></div>
  <p class="welcome-copy">On the other hand, we denounce with righteous indignation and dislike men who are so beguiled and demoralized by the charms of pleasure of the moment, so blinded by desire, that they cannot foresee the pain and trouble that are bound to ensue; and equal blame belongs to those who fail in their duty through weakness of will, which is the same as saying through shrinking from toil and pain. These cases are perfectly simple.</p>
  <a class="btn-double"><span>READ MORE</span></a>
</section>

<section class="industries">
  <h2 class="section-title" style="top:46px;color:var(--paper)">INDUSTRIES</h2>
  <div class="section-bar" style="top:97px"></div>
  <article class="industry-card" style="left:132px">
    <div class="industry-photo" role="img" aria-label="Business team discussing work around a laptop in a bright office" style="background:linear-gradient(135deg,#9aa7b0,#5d6870)"></div>
    <h4>LOREM IPSUM</h4>
    <p>Lorem ipsum dolor sit amet, conse ctetur adipiscing elit, sed do eiusmod.</p>
  </article>
  <article class="industry-card" style="left:371px">
    <div class="industry-photo" role="img" aria-label="Hands working with a calculator and pen on paperwork" style="background:linear-gradient(135deg,#e9e7e4,#7d7a76)"></div>
    <h4>LOREM IPSUM</h4>
    <p>Lorem ipsum dolor sit amet, conse ctetur adipiscing elit, sed do eiusmod.</p>
  </article>
  <article class="industry-card" style="left:611px">
    <div class="industry-photo" role="img" aria-label="Crumpled yellow paper light bulb idea on a dark chalkboard" style="background:radial-gradient(circle at 50% 45%,#c9a52a 0,#5a4d24 18%,#1b1b1b 45%)"></div>
    <h4>LOREM IPSUM</h4>
    <p>Lorem ipsum dolor sit amet, conse ctetur adipiscing elit, sed do eiusmod.</p>
  </article>
  <article class="industry-card" style="left:850px">
    <div class="industry-photo" role="img" aria-label="Hand with pen reviewing blue financial charts on paper" style="background:linear-gradient(135deg,#f4f4f6,#c9cfe0)"></div>
    <h4>LOREM IPSUM</h4>
    <p>Lorem ipsum dolor sit amet, conse ctetur adipiscing elit, sed do eiusmod.</p>
  </article>
  <a class="btn-light"><span>VIEW ALL INDUSTRIES</span></a>
</section>

<section class="success">
  <h2 class="section-title" style="top:46px">SUCCESS STORIES</h2>
  <div class="section-bar" style="top:99px"></div>
</section>
<div class="quote-shadow"></div>
<div class="quote-card">
  <span class="quote-glyph" style="left:10px;top:-12px">&ldquo;</span>
  <span class="quote-glyph" style="left:866px;top:208px">&rdquo;</span>
  <p class="quote-text" style="left:68px">Lorem ipsum dolor sit amet, consectetur adipiscing elit, sed do eiusmod tempor inci didunt ut labore et dolore magna aliqua Ut enim ad minim veniam, quis nostrud exercitation ullamco laboris nisi ut aliquip ex ea commodo consequat. Duis aute irure dolor in eprehend erit in voluptate velit esse.</p>
  <div class="quote-divider"></div>
  <p class="quote-author" style="left:127px">RICHARD<small>Manager</small></p>
  <p class="quote-text" style="left:555px">Lorem ipsum dolor sit amet, consectetur adipiscing elit, sed do eiusmod tempor inci didunt ut labore et dolore magna aliqua Ut enim ad minim veniam, quis nostrud exercitation ullamco laboris nisi ut aliquip ex ea commodo consequat. Duis aute irure dolor in eprehend erit in voluptate velit esse.</p>
  <p class="quote-author" style="left:614px">RICHARD<small>Manager</small></p>
</div>
<span class="dot" style="left:547px"></span>
<span class="dot" style="left:571px"></span>
<span class="dot on" style="left:596px"></span>
<span class="dot" style="left:620px"></span>
<span class="dot" style="left:641px"></span>

<footer class="footer">
  <svg class="abs" style="left:0;top:-12px" width="1200" height="16" viewBox="0 0 1200 16" preserveAspectRatio="none"><path fill="#000" d="M0 10l20-4 18 5 25-6 30 4 22-5 28 6 24-3 30 4 26-6 22 5 30-3 26 4 24-6 28 5 30-4 22 6 26-5 30 3 24-4 28 5 22-6 30 5 26-3 24 4 28-6 30 5 22-4 26 6 30-5 24 3 28-4 22 5 30-6 26 4 24-3 28 5 30-4 22 6 26-5 30 3 24-4 28 5 22-6 30 4 26 3 24-5 28 4 30-3 18 4V16H0z"/></svg>
  <div class="footer-mark"><span>Brackenfield<br>Partners</span></div>

  <h5 style="left:410px">FOLLOW US</h5>
  <div class="social" style="top:136px"><i></i><span>Like us on<br>FRIENDLANE</span></div>
  <div class="social" style="top:198px"><i></i><span>Follow us on<br>CHIRPLINE</span></div>
  <div class="social" style="top:259px"><i></i><span>Follow us on<br>PROFLINK</span></div>

  <h5 style="left:654px">MENU</h5>
  <ul class="footer-menu">
    <li>Home</li><li>About Us</li><li>Services</li><li>Industries</li><li>Our Success</li><li>Contact.</li>
  </ul>

  <h5 style="left:858px">CONTACT US</h5>
  <div class="contact-item" style="top:144px"><i><svg width="18" height="18" viewBox="0 0 24 24" fill="#000"><path d="M6.6 10.8a15 15 0 0 0 6.6 6.6l2.2-2.2a1 1 0 0 1 1-.25 11 11 0 0 0 3.6.6 1 1 0 0 1 1 1V20a1 1 0 0 1-1 1A17 17 0 0 1 3 4a1 1 0 0 1 1-1h3.5a1 1 0 0 1 1 1 11 11 0 0 0 .6 3.6 1 1 0 0 1-.25 1z"/></svg></i><span>CALL US<br><b>888.888.8888</b></span></div>
  <div class="contact-item" style="top:210px"><i><svg width="16" height="16" viewBox="0 0 24 24" fill="#000"><path d="M2 5h20v14H2z"/><path d="M2 5l10 8 10-8" fill="none" stroke="#fff" stroke-width="2"/></svg></i><span>E MAIL US<br><b>info@brackenfieldpartners.com</b></span></div>

  <div class="footer-rule"></div>
  <p class="copyright">Copyright © 2020 All Rights Reserved</p>
</footer>

</body>
</html>
```